COMPANY SIGN

I am in the process of ordering new company For Sale signs and stationary (business cards, envelopes, letterheads, and labels). I need a new design with my existing company logo. The TWO MOST IMPORTANT PROJECTS I need right now is the new design for the company sign and business cards. I've uploaded a .jpg file of my company logo.

I like the design to be eye catching and the background color of the company sign to be soothing to the eyes. Perhaps, using one of the color on the leaves of the logo or any other color that the designer think will go well with the logo. My favorite colors are teal or light olive color but don't let that affect your creativity.

Industry/Entity Type

Business

Requirements
Should not have
• Please don't use "Times New Roman" fonts or fonts that is hard to read.

```html
<!DOCTYPE html>
<html lang="en">
<head>
<meta charset="utf-8">
<title>For Sale Sign – Maplewood Home Group</title>
<link rel="stylesheet" href="https://fonts.googleapis.com/css2?family=Comfortaa:wght@300&family=Source+Sans+3:wght@400;600&family=PT+Serif:wght@700&display=swap">
<style>
  :root {
    --olive: #768845;
    --lime: #bdc956;
    --brown: #5b4431;
    --sky: #7ab3d8;
    --white: #ffffff;
    --edge: #3a3a3a;
  }
  html, body {
    margin: 0;
    padding: 0;
    overflow: hidden;
    background: var(--white);
  }
  .sign {
    position: relative;
    width: 1200px;
    height: 903px;
    box-sizing: border-box;
    border: 1.5px solid var(--edge);
    background: var(--white);
    overflow: hidden;
  }
  .headline {
    position: absolute;
    top: 12px;
    left: 0;
    width: 100%;
    margin: 0;
    text-align: center;
    font-family: "Comfortaa", sans-serif;
    font-weight: 300;
    font-size: 190px;
    line-height: 1;
    letter-spacing: 3px;
    color: var(--olive);
    white-space: nowrap;
  }
  .brand-mark {
    position: absolute;
    left: 537px;
    top: 218px;
    width: 150px;
    height: 150px;
    border-radius: 50%;
    background: var(--lime);
  }
  .stripe-top {
    position: absolute;
    top: 391px;
    left: 0;
    width: 100%;
    height: 26px;
    background: var(--lime);
  }
  .brand-band {
    position: absolute;
    top: 417px;
    left: 0;
    width: 100%;
    height: 304px;
    background: var(--brown);
    text-align: center;
    font-family: "Source Sans 3", sans-serif;
  }
  .brand-name {
    margin: 58px 0 0;
    font-weight: 400;
    font-size: 104px;
    line-height: 1.1;
    color: var(--white);
    white-space: nowrap;
  }
  .tagline {
    margin: 46px 0 0;
    font-size: 46px;
    line-height: 1;
    font-weight: 600;
    color: var(--lime);
    white-space: nowrap;
  }
  .stripe-bottom {
    position: absolute;
    top: 721px;
    left: 0;
    width: 100%;
    height: 28px;
    background: var(--sky);
  }
  .contact {
    position: absolute;
    top: 764px;
    left: 53px;
    margin: 0;
    white-space: nowrap;
    color: var(--brown);
    line-height: 1;
  }
  .contact-label {
    font-family: "Source Sans 3", sans-serif;
    font-size: 50px;
    font-weight: 400;
  }
  .contact-phone {
    font-family: "PT Serif", serif;
    font-weight: 700;
    font-size: 92px;
    margin-left: 8px;
  }
</style>
</head>
<body>
  <main class="sign">
    <h1 class="headline">FOR SALE</h1>
    <div class="brand-mark" aria-hidden="true"></div>
    <div class="stripe-top"></div>
    <section class="brand-band">
      <p class="brand-name">Maplewood Home Group</p>
      <p class="tagline">Helping Families Find Their Way Home</p>
    </section>
    <div class="stripe-bottom"></div>
    <p class="contact">
      <span class="contact-label">For a showing call:</span>
      <span class="contact-phone">(555) 014-2700</span>
    </p>
  </main>
</body>
</html>
```